Rebrand stationary with recently completed logo design

Need new business cards, thank you cards, letterhead, envelopes and presentation folders. The designs will be sent to a separate production firm so I need the files to be print ready.

My contact info
Reno Vasquell

Office 604-381-5047
Fax 604-317-4860

Email reno@glazemark.ca
website www.glazemark.ca

315-20740 47th Avenue,
Langley, BC, V2K 3P8

Target Market(s)

Homeowners, businesses and contractors

Industry/Entity Type

Business

Font styles to use
Sans Serif

Colors
34a7d7

Requirements
Must have
• Like to have one side of the business card a solid color with the logo in all white. The side with all the text to be a white background
• I find the current blue on the front of the card with the white logo too dark.
Should not have
• Gradient colors

```html
<!DOCTYPE html>
<html lang="en">
<head>
<meta charset="utf-8">
<title>Glazemark Letterhead</title>
<link href="https://fonts.googleapis.com/css2?family=Arimo:wght@400&family=Fira+Sans:ital,wght@0,400;1,400&display=swap" rel="stylesheet">
<style>
  :root{
    --backdrop:#e6e7e9;
    --paper:#ffffff;
    --brand-blue:#1e9ad6;
    --ink:#4d4d4f;
    --body-ink:#58595b;
    --mark-grey:#4a5560;
    --signature-tone:#8a8b8d;
  }
  *{margin:0;padding:0;box-sizing:border-box}
  html,body{width:856px;height:1200px;overflow:hidden;background:var(--backdrop)}
  .canvas{position:relative;width:856px;height:1200px}
  .letterhead{position:absolute;left:43px;top:57px;width:777px;height:1099px;background:var(--paper);overflow:hidden}
  .corner-wave{position:absolute;left:0;top:0}
  .brand{position:absolute;left:34px;top:112px;display:flex;align-items:center;gap:10px}
  .brand-square{width:22px;height:22px;background:var(--brand-blue)}
  .brand-name{font-family:"Fira Sans",sans-serif;font-weight:400;font-size:30px;letter-spacing:1px;color:var(--brand-blue)}
  .contact{position:absolute;left:565px;top:52px;list-style:none;font-family:"Fira Sans",sans-serif;font-style:italic;font-size:14.5px;color:var(--ink);line-height:19.5px}
  .contact li{display:flex;align-items:flex-start;gap:6px}
  .contact svg{flex:none;margin-top:4px}
  .letter-body{position:absolute;left:120px;top:255px;width:520px;font-family:"Arimo",sans-serif;font-size:13.4px;line-height:19.2px;color:var(--body-ink)}
  .letter-body p{margin-bottom:19.2px}
  .signature{position:absolute;left:118px;top:815px;width:130px;height:64px;background:var(--signature-tone);opacity:.35;border-radius:4px}
  .sign-off{position:absolute;left:120px;top:884px;font-family:"Arimo",sans-serif;font-size:13.4px;line-height:19.2px;color:var(--body-ink)}
  .website{position:absolute;left:36px;top:1040px;display:flex;align-items:center;gap:8px;font-family:"Fira Sans",sans-serif;font-style:italic;font-size:20px;color:var(--brand-blue)}
</style>
</head>
<body>
<div class="canvas">
  <div class="letterhead">
    <svg class="corner-wave" width="777" height="1099" viewBox="0 0 777 1099" aria-hidden="true">
      <path d="M444 1099 C600 1085 698 1010 697 900 L695 874 C720 900 748 905 777 893 L777 1099 Z" fill="var(--brand-blue)"/>
    </svg>

    <div class="brand">
      <span class="brand-square"></span>
      <span class="brand-name">GLAZEMARK</span>
    </div>

    <ul class="contact">
      <li><svg width="12" height="12" viewBox="0 0 12 12"><path d="M2 1l2 0 1 3-1.5 1a6 6 0 0 0 3.5 3.5L8 7l3 1v2a1 1 0 0 1-1 1A9 9 0 0 1 1 2a1 1 0 0 1 1-1z" fill="none" stroke="var(--brand-blue)" stroke-width="1"/></svg>604-381-5047</li>
      <li><svg width="12" height="12" viewBox="0 0 12 12"><rect x="2" y="1" width="8" height="10" fill="none" stroke="var(--brand-blue)"/><path d="M4 4h4M4 6h4M4 8h4" stroke="var(--brand-blue)"/></svg>604-317-4860</li>
      <li><svg width="13" height="12" viewBox="0 0 13 12"><rect x="1" y="2.5" width="11" height="8" fill="none" stroke="var(--brand-blue)"/><path d="M1 2.5l5.5 4.5 5.5-4.5" fill="none" stroke="var(--brand-blue)"/></svg>reno@glazemark.ca</li>
      <li><svg width="12" height="13" viewBox="0 0 12 13"><path d="M6 12C3 8 2 6.5 2 5a4 4 0 0 1 8 0c0 1.5-1 3-4 7z" fill="none" stroke="var(--brand-blue)"/><circle cx="6" cy="5" r="1.5" fill="none" stroke="var(--brand-blue)"/></svg><span>315-20740 47th Avenue,<br>Langley, BC, V2K 3P8</span></li>
    </ul>

    <div class="letter-body">
      <p>Contrary to popular belief, Lorem Ipsum is not simply random text. It has roots in a piece of classical Latin literature from 45 BC, making it over 2000 years old. Howard Pellister, a Latin professor at Ashgrove College in Virginia, looked up one of the more obscure Latin words, consectetur, from a Lorem Ipsum passage, and going through the cites of the word in classical literature, discovered the undoubtable source. Lorem Ipsum comes from sections 1.10.32 and 1.10.33 of "de Finibus Bonorum et Malorum" (The Extremes of Good and Evil) by Aurelian Tesk, written in 45 BC. This book is a treatise on the theory of ethics, very popular during the Renaissance. The first line of Lorem Ipsum, "Lorem ipsum dolor sit amet..", comes from a line in section 1.10.32.</p>
      <p>The standard chunk of Lorem Ipsum used since the 1500s is reproduced below for those interested. Sections 1.10.32 and 1.10.33 from "de Finibus Bonorum et Malorum" by Aurelian Tesk are also reproduced in their exact original form, accompanied by English versions from the 1914 translation by J. Morrow.</p>
      <p>Where can I get some?<br>There are many variations of passages of Lorem Ipsum available, but the majority have suffered alteration in some form, by injected humour, or randomised words which don't look even slightly believable. If you are going to use a passage of Lorem Ipsum, you need to be sure there isn't anything embarrassing hidden in the middle of text. All the Lorem Ipsum generators on the Internet tend to repeat predefined chunks as necessary, making this the first true generator on the Internet. It uses a dictionary of over 200 Latin words, combined with a handful of model sentence structures, to generate Lorem Ipsum which looks reasonable. The generated Lorem Ipsum is therefore always free from repetition, injected humour, or non-characteristic words etc.</p>
    </div>

    <div class="signature" role="img" aria-label="Handwritten signature"></div>
    <div class="sign-off">‘Lorem<br>ipsum dolor sit amet...’<br>Generate Lorem Ipsum</div>

    <div class="website">
      <svg width="14" height="14" viewBox="0 0 14 14" aria-hidden="true"><circle cx="7" cy="7" r="6" fill="none" stroke="var(--brand-blue)"/><ellipse cx="7" cy="7" rx="2.6" ry="6" fill="none" stroke="var(--brand-blue)"/><path d="M1 7h12M2 4h10M2 10h10" stroke="var(--brand-blue)" stroke-width=".8"/></svg>
      www.glazemark.ca
    </div>
  </div>
</div>
</body>
</html>
```